Verdane Kiwi Root Essence Prime Serum - Product Label

Hi Guys,

I threw up a rough label sketch. Looking to keep the label clean and fresh.

LABEL DIMENSIONS: 4.05 in (Height) x 1.18 in (Diameter)

Industry/Entity Type

Beauty Aid

Font styles to use
Serif

Colors
0255a3
0592cd
6b449b
ffc214

Requirements
Must have
• Lumivelle
• __________
• S K I N
Nice to have
• We can try purple, gold and black or stick with the blue scheme we have going.

```html
<!DOCTYPE html>
<html lang="en">
<head>
<meta charset="utf-8">
<title>Verdane Kiwi Root Essence Prime Serum – Label</title>
<link rel="stylesheet" href="https://fonts.googleapis.com/css2?family=PT+Sans:wght@400;700&family=PT+Sans+Narrow&display=swap">
<style>
  :root {
    --ink-blue: #0d4a9c;
    --text-blue: #1b55a6;
    --teal: #35b3cc;
    --teal-light: #6fcadb;
    --paper: #ffffff;
    --edge: #c9cdd3;
  }
  * { margin: 0; padding: 0; box-sizing: border-box; }
  html, body { width: 1200px; height: 927px; overflow: hidden; background: var(--paper); }
  body { position: relative; font-family: "PT Sans", Arial, sans-serif; color: var(--text-blue); }

  .label {
    position: absolute; left: 40px; top: 222px; width: 1112px; height: 498px;
    border: 1.5px solid var(--edge); border-radius: 18px; overflow: hidden; background: var(--paper);
  }
  .label-wave { position: absolute; left: 0; top: 0; width: 1112px; height: 498px; }

  .ingredients, .directions {
    position: absolute; left: 22px; width: 263px;
    font-family: "PT Sans Narrow", "Arial Narrow", sans-serif;
    font-size: 13.5px; line-height: 17px; text-align: justify; hyphens: auto;
  }
  .ingredients { top: 51px; }
  .directions { top: 290px; }

  .brand {
    position: absolute; left: 300px; top: 48px; width: 500px;
    display: flex; flex-direction: column; align-items: center;
  }
  .brand-dot { width: 62px; height: 62px; border-radius: 50%; background: var(--teal); margin-bottom: 18px; }
  .brand-name {
    font-size: 58px; letter-spacing: 9px; color: var(--ink-blue); font-weight: 400; line-height: 1;
  }

  .product {
    position: absolute; left: 300px; top: 240px; width: 500px; text-align: center; color: var(--ink-blue);
  }
  .product-line1 { font-size: 35px; font-weight: 700; line-height: 38px; letter-spacing: 0.5px; }
  .product-line2 { font-size: 29px; font-weight: 400; line-height: 34px; letter-spacing: 0.5px; }
  .product-type {
    display: inline-block; margin-top: 10px; padding: 0 16px; background: var(--teal);
    color: var(--paper); font-size: 25px; line-height: 28px; letter-spacing: 1px;
  }

  .volume {
    position: absolute; left: 300px; top: 430px; width: 500px; text-align: center;
    color: var(--paper); font-size: 20px; letter-spacing: 0.5px;
  }

  .distributor {
    position: absolute; left: 880px; top: 103px; width: 170px; text-align: center;
    font-size: 19px; line-height: 24px; color: var(--text-blue);
  }
  .distributor p + p { margin-top: 2px; }
  .distributor .addr { margin-top: 10px; }

  .certs { position: absolute; left: 843px; top: 255px; display: flex; gap: 12px; }
  .cert { width: 72px; height: 72px; border-radius: 50%; border: 1.5px solid var(--ink-blue); }

  .barcode-area {
    position: absolute; left: 836px; top: 345px; width: 255px; height: 115px;
    background: var(--paper); border: 1.5px solid #555;
    display: flex; align-items: center; justify-content: center;
    font-size: 30px; color: #111;
  }
</style>
</head>
<body>
  <main class="label">
    <svg class="label-wave" viewBox="0 0 1112 498" aria-hidden="true">
      <path d="M0 425 C 150 455, 330 460, 560 430 S 900 385, 1112 385 L1112 498 L0 498 Z" fill="var(--teal)"/>
      <path d="M0 418 C 150 447, 330 452, 560 422 S 900 378, 1112 378" fill="none" stroke="var(--teal-light)" stroke-width="3"/>
      <path d="M0 410 C 150 440, 330 445, 560 414 S 900 370, 1112 370" fill="none" stroke="var(--ink-blue)" stroke-width="5"/>
    </svg>

    <p class="ingredients">Ingredient List: Purified water, (VerdaCell Root Cell), Actinidia Chinensis, Glycerin, Lecithin, Phenoxyethanol, Collagen, Palmitol, Tetrapeptide-3, (Peptilex 3000), Propylene Glycol, Polyglutamic Acid, Phenoxythanol, Hydroxyethylcellulose, Propylene Glycol, Benzylalcohol, Dehydroacetic Acid.</p>

    <p class="directions">How to Use: Wash area where you will apply the Verdane Kiwi Root Essence Serum thoroughly. Apply the product and let absorb for 15 minutes then apply moisturizer if desired.</p>

    <div class="brand">
      <span class="brand-dot"></span>
      <span class="brand-name">AURELANE RX</span>
    </div>

    <div class="product">
      <h1 class="product-line1">VERDANE KIWI ROOT</h1>
      <h2 class="product-line2">ESSENCE PRIME</h2>
      <span class="product-type">SERUM</span>
    </div>

    <p class="volume">1 fl. oz / 30 ml</p>

    <div class="distributor">
      <p>Distributed by:</p>
      <p>Aurelane Rx</p>
      <p class="addr">Address</p>
      <p>website</p>
    </div>

    <div class="certs">
      <span class="cert"></span>
      <span class="cert"></span>
      <span class="cert"></span>
    </div>

    <div class="barcode-area">BARCODE</div>
  </main>
</body>
</html>
```